Infografik im Bereich Artikelbeschreibung für Onlineshop
Zielgruppe
Vertrieb von Saunaaustattung
Aufgabenstellung
Wird als Ergänzung für die Artikelbeschreibung im Webshop benötigt.
Ein Beispiel wo die Infografik platziert werden soll:
https://www.wolkenkessel-shop.de/Bilder/beispiel.jpg
Bildgröße ca. 1200 x 800 px
Als Hintergrund eventuell möglich teilweise oder ganz die Grafik mit den blauen Wassertropfen verwendbar?

```html
<!DOCTYPE html>
<html lang="de">
<head>
<meta charset="utf-8">
<title>Dampfgenerator – Ausstattungsmerkmale</title>
<link rel="stylesheet" href="https://fonts.googleapis.com/css2?family=Roboto+Condensed:wght@700&display=swap">
<style>
:root{
  --bg-top:#cfe6f3;
  --bg-mid:#7fb6d6;
  --bg-low:#2f78ad;
  --blue:#1e8fd8;
  --blue-dark:#1565b0;
  --blue-light:#52bbea;
  --white:#ffffff;
  --text-dark:#1a5fa8;
  --line:#ffffff;
}
*{box-sizing:border-box;margin:0;padding:0}
html,body{width:1200px;height:800px;overflow:hidden}
body{font-family:"Roboto Condensed",Arial Narrow,sans-serif;font-weight:700}
.canvas{position:relative;width:1200px;height:800px;overflow:hidden;
  background:radial-gradient(ellipse at 50% 30%,var(--bg-top) 0%,var(--bg-mid) 45%,var(--bg-low) 100%)}
.connectors{position:absolute;inset:0}
.pill{position:absolute;height:90px;display:flex;align-items:center;text-transform:uppercase;font-size:21px;line-height:1.3;box-shadow:0 3px 8px rgba(0,40,90,.25)}
.pill.left{left:0;width:325px;border-radius:0 45px 45px 0;padding-left:30px}
.pill.right{right:0;width:345px;border-radius:45px 0 0 45px;padding-left:115px}
.fill-blue{background:var(--blue);color:var(--white)}
.fill-dark{background:var(--blue-dark);color:var(--white)}
.fill-light{background:var(--blue-light);color:var(--white)}
.fill-white{background:var(--white);color:var(--text-dark)}
.icon-disc{position:absolute;width:76px;height:76px;border-radius:50%;background:var(--white);display:flex;align-items:center;justify-content:center}
.pill.left .icon-disc{right:7px;top:7px}
.pill.right .icon-disc{left:7px;top:7px;border:3px solid var(--white)}
.fill-white .icon-disc{border:2px solid #d7e8f4}
.part-photo{width:100%;height:100%;border-radius:50%;background:radial-gradient(circle at 40% 40%,#f2f2f2,#9a9a9a 70%,#555)}
.icon-disc svg{width:46px;height:46px;stroke:var(--blue);fill:none;stroke-width:2.2;stroke-linecap:round;stroke-linejoin:round}
.tab{position:absolute;width:86px;display:flex;flex-direction:column;align-items:center;text-transform:uppercase;color:var(--white);font-size:9.5px;line-height:1.25;text-align:center;box-shadow:0 3px 8px rgba(0,40,90,.25)}
.tab.top{top:0;height:137px;border-radius:0 0 43px 43px;padding-top:18px;justify-content:space-between;padding-bottom:6px}
.tab.bottom{bottom:0;height:160px;border-radius:43px 43px 0 0;padding-top:8px;padding-bottom:22px;justify-content:space-between}
.tab .icon-disc{position:static;width:72px;height:72px}
.tab .icon-disc svg{width:44px;height:44px}
.tab.fill-dark .icon-disc svg{stroke:var(--blue-dark)}
.hub{position:absolute;left:380px;top:180px;width:440px;height:440px;border-radius:50%;background:var(--blue);display:flex;align-items:center;justify-content:center;box-shadow:0 4px 14px rgba(0,40,90,.3)}
.hub-inner{width:404px;height:404px;border-radius:50%;background:var(--white);display:flex;align-items:center;justify-content:center}
.product-photo{width:360px;height:360px;border-radius:50%;background:radial-gradient(circle at 45% 45%,#f4f4f4 0%,#d0d2d4 45%,#a7aaad 70%,#ffffff 72%)}
</style>
</head>
<body>
<main class="canvas">
  <svg class="connectors" viewBox="0 0 1200 800" aria-hidden="true">
    <g stroke="var(--line)" stroke-width="4">
      <line x1="320" y1="160" x2="600" y2="400"/>
      <line x1="320" y1="275" x2="600" y2="400"/>
      <line x1="320" y1="395" x2="600" y2="400"/>
      <line x1="320" y1="520" x2="600" y2="400"/>
      <line x1="320" y1="640" x2="600" y2="400"/>
      <line x1="880" y1="160" x2="600" y2="400"/>
      <line x1="880" y1="275" x2="600" y2="400"/>
      <line x1="880" y1="395" x2="600" y2="400"/>
      <line x1="880" y1="520" x2="600" y2="400"/>
      <line x1="880" y1="640" x2="600" y2="400"/>
    </g>
  </svg>

  <div class="hub"><div class="hub-inner">
    <div class="product-photo" role="img" aria-label="Produktfoto: Dampfgenerator mit Edelstahlgehäuse und Anschlüssen"></div>
  </div></div>

  <!-- top features -->
  <div class="tab top fill-blue" style="left:328px">Thermoschutz
    <div class="icon-disc"><svg viewBox="0 0 48 48"><path d="M24 5l15 6v11c0 10-7 17-15 21C16 39 9 32 9 22V11z"/><path d="M24 14v14"/><circle cx="24" cy="31" r="4"/></svg></div>
  </div>
  <div class="tab top fill-light" style="left:468px;width:92px">Automatische Selbstreinigung
    <div class="icon-disc"><svg viewBox="0 0 48 48"><path d="M36 8L24 24"/><path d="M16 22l10 8-6 10c-6-2-10-6-12-12z"/><circle cx="34" cy="38" r="1.5"/><circle cx="39" cy="32" r="1.5"/></svg></div>
  </div>
  <div class="tab top fill-blue" style="left:608px">Kompakte Größe
    <div class="icon-disc"><svg viewBox="0 0 48 48"><path d="M10 8v30h30"/><path d="M16 8h24v24" stroke-dasharray="3 3"/><text x="18" y="28" font-size="10" fill="var(--blue)" stroke="none" font-family="Arial,sans-serif">cm²</text></svg></div>
  </div>
  <div class="tab top fill-dark" style="left:762px">Gerät kocht auf ca. 100 C° hoch
    <div class="icon-disc"><svg viewBox="0 0 48 48"><circle cx="24" cy="24" r="18"/><circle cx="24" cy="24" r="7"/><path d="M24 11v6M24 31v6M11 24h6M31 24h6M12 12l24 24"/></svg></div>
  </div>

  <!-- left features -->
  <div class="pill left fill-blue" style="top:113px">Inkludierte<br>Armoaauslassdüse
    <div class="icon-disc"><svg viewBox="0 0 48 48"><circle cx="24" cy="20" r="8"/><path d="M24 8v4M14 34l-3 5M24 34v6M34 34l3 5"/></svg></div>
  </div>
  <div class="pill left fill-white" style="top:230px">Kurze Aufheizzeit
    <div class="icon-disc"><svg viewBox="0 0 48 48"><path d="M10 18A16 16 0 1 1 10 30" stroke-dasharray="3 3"/><path d="M6 14l4 4 4-4"/><text x="15" y="24" font-size="9" fill="var(--blue)" stroke="none" font-family="Arial,sans-serif">4 - 8</text><text x="16" y="33" font-size="8" fill="var(--blue)" stroke="none" font-family="Arial,sans-serif">min</text></svg></div>
  </div>
  <div class="pill left fill-dark" style="top:350px">Ansteuerung von bis<br>zu zwei Duftstoffen
    <div class="icon-disc"><svg viewBox="0 0 48 48"><circle cx="12" cy="28" r="5"/><circle cx="24" cy="26" r="7"/><circle cx="36" cy="28" r="5"/></svg></div>
  </div>
  <div class="pill left fill-light" style="top:475px">Optional<br>Steuerung per App
    <div class="icon-disc"><svg viewBox="0 0 48 48"><rect x="12" y="6" width="22" height="34" rx="3"/><path d="M22 36h2"/><path d="M26 22v12l8 6"/></svg></div>
  </div>
  <div class="pill left fill-white" style="top:598px">Elektronische<br>Entkalkung
    <div class="icon-disc"><svg viewBox="0 0 48 48"><path d="M18 6v10M24 4v12M30 6v10"/><path d="M14 24l10 16 10-16"/><circle cx="20" cy="26" r="2"/><circle cx="27" cy="28" r="2"/></svg></div>
  </div>

  <!-- right features -->
  <div class="pill right fill-blue" style="top:118px">Manuelles<br>Entkalken
    <div class="icon-disc"><div class="part-photo" role="img" aria-label="Foto: Entkalkungsanschluss"></div></div>
  </div>
  <div class="pill right fill-white" style="top:230px">Gehäuse<br>Edelstahl<br>S304
    <div class="icon-disc"><div class="part-photo" role="img" aria-label="Foto: Edelstahlgehäuse"></div></div>
  </div>
  <div class="pill right fill-blue" style="top:350px">Hochleistungs-<br>heizstäbe
    <div class="icon-disc"><div class="part-photo" role="img" aria-label="Foto: Heizstab"></div></div>
  </div>
  <div class="pill right fill-light" style="top:475px">Elektronisches<br>Abflussventil
    <div class="icon-disc"><div class="part-photo" role="img" aria-label="Foto: Abflussventil"></div></div>
  </div>
  <div class="pill right fill-white" style="top:578px;height:120px;border-radius:60px 0 0 60px">Steuerdisplay<br>fliesenbündig<br>einbaubar</div>

  <!-- bottom features -->
  <div class="tab bottom fill-light" style="left:328px">
    <div class="icon-disc"><svg viewBox="0 0 48 48"><path d="M17 28a11 11 0 1 1 14 0v6H17z"/><path d="M18 38h12M20 42h8"/></svg></div>Farblichtsteuerung
  </div>
  <div class="tab bottom fill-light" style="left:468px;width:92px">
    <div class="icon-disc"><svg viewBox="0 0 48 48"><path d="M16 10l18 8-8 16-14-6z"/><circle cx="16" cy="38" r="1.5"/><circle cx="22" cy="42" r="1.5"/></svg></div>Ansteuerung Salzsolevernebler
  </div>
  <div class="tab bottom fill-light" style="left:608px">
    <div class="icon-disc"><svg viewBox="0 0 48 48"><path d="M20 8a4 4 0 0 1 8 0v22a8 8 0 1 1-8 0z"/><path d="M24 16v18"/></svg></div>Verbrühschutz Abfluss
  </div>
  <div class="tab bottom fill-dark" style="left:762px">
    <div class="icon-disc"><svg viewBox="0 0 48 48"><circle cx="24" cy="24" r="18"/><circle cx="24" cy="24" r="3"/><path d="M24 21c-2-6 0-10 5-10 2 4-1 8-5 10zM27 25c6 1 8 5 5 9-5 0-6-5-5-9zM21 26c-4 5-9 5-10 0 2-4 7-4 10 0z"/></svg></div>Integrierte Abluftsteuerung
  </div>
</main>
</body>
</html>
```